International Website Security StartUp needs a banner ads design

We need an advertisement of our product and company "GuardNestly" that we can use in blogs and communities around WordPress.
We want the ad to communicate that you need a website security solution and that if you are looking for one, ours is the best on the market.
The ad should use our basic colors (white, red, black, grey) or shades/variations of this. It should not look to dark, but friendly and helpful. No animation please.
I need a banner design for display advertising campaign. Sizes needed are as follows:
234x60
160 x 600
125x125
250 x 250
300 x 250
468 x 60
728 x 90
Our product is a website security suite which comes in four editions. Pricing starts at $10/month.
Our solution helps basically every website owner to protect his website/blog/online business against hackers and malware attacks.
Other then other solutions we have an AI engine which even can find never before seen malware and finds around 40% more malware then signature based approaches. These AI engine was even funded by the Federal research council of Verdania as one of the upcoming and outstanding technologies to make the internet safer.
Our solution (depending on the edition) includes Blacklist and reputation Monitoring, Speed & Uptime Monitoring for the website, Standard and Advanced Malware Monitoring. We also offer Vulnerability Assessments and Friendbook Wall Protection within the packages. Best of all is that we have an automated malware cleanup included in the product, so that also not technical people can use our software and their site is cleaned from malware automatically even if they don't know how to do that, as we do it for them. Fully automated the moment malware is discovered on the page, without submitting a support ticket and waiting for feedback.
The scan frequency of our product varies from weekly to continuously.
To read more about our product and company have a look at www.guardnestly-example.com.
Target Market(s)
WordPress Users, Designer & WebAgencies looking for a website security solution
Industry/Entity Type
Advertising

```html
<!DOCTYPE html>
<html lang="en">
<head>
<meta charset="utf-8">
<title>GuardNestly – Banner Set</title>
<link rel="stylesheet" href="https://fonts.googleapis.com/css2?family=Open+Sans:wght@400;600;700;800&display=swap">
<style>
  :root{
    --stage-centre:#767676;
    --stage-edge:#262626;
    --ink-dark:#1b1b1b;
    --panel-dark:#2b2b2b;
    --panel-dark-top:#4a4a4a;
    --red:#b3161c;
    --red-deep:#7c1014;
    --red-bright:#d8353a;
    --grey-light:#e6e6e6;
    --grey-mid:#bdbdbd;
    --grey-feature:#9a9a9a;
    --grey-feature-dark:#6f6f6f;
    --white:#ffffff;
    --label:#d9d9d9;
    --sans:"Open Sans", Arial, sans-serif;
  }
  *{box-sizing:border-box;margin:0;padding:0}
  html,body{width:1200px;height:827px;overflow:hidden}
  body{
    font-family:var(--sans);
    background:radial-gradient(ellipse 60% 60% at 55% 45%, var(--stage-centre), var(--stage-edge));
    position:relative;
  }
  .banner{position:absolute;overflow:hidden}
  .size-label{
    position:absolute;width:200px;text-align:center;
    color:var(--label);font-size:28px;font-weight:400;
  }
  .brand-mark{
    border-radius:50%;
    background:radial-gradient(circle at 50% 40%, var(--red-bright), var(--red) 60%, var(--red-deep));
    position:absolute;
  }
  .brand-name{color:var(--white);font-weight:700;position:absolute;white-space:nowrap;letter-spacing:-0.2px}
  .headline{font-weight:800;line-height:1;text-transform:uppercase;letter-spacing:-0.3px}
  .btn-learn{
    position:absolute;display:flex;align-items:center;justify-content:center;
    color:var(--white);font-weight:700;border-radius:5px;letter-spacing:0.3px;
    background:linear-gradient(var(--red-bright),var(--red) 55%,var(--red-deep));
    box-shadow:0 2px 3px rgba(0,0,0,.45);
  }
  .btn-learn.is-dark{background:linear-gradient(#777,#3b3b3b 55%,#222)}
  .feature-list{list-style:none;position:absolute;color:var(--white)}
  .feature-list li{display:flex;align-items:center;white-space:nowrap}
  .feature-list svg{width:17px;height:17px;margin-right:12px;flex:none}
  .rule{position:absolute;height:2px;background:var(--red-deep)}

  /* 160 x 600 skyscraper */
  .sky{left:64px;top:55px;width:180px;height:674px;background:var(--ink-dark)}
  .sky-top{position:absolute;left:0;top:0;width:180px;height:211px;background:linear-gradient(var(--panel-dark-top),var(--panel-dark) 70%,#161616)}
  .sky-top .brand-mark{left:12px;top:20px;width:156px;height:156px}
  .sky-top .brand-name{left:0;width:180px;text-align:center;top:178px;font-size:23px}
  .sky-redline{position:absolute;left:0;top:211px;width:180px;height:5px;background:var(--red)}
  .sky-body{position:absolute;left:0;top:216px;width:180px;height:272px;background:linear-gradient(var(--white),var(--grey-light) 50%,var(--grey-mid));color:var(--ink-dark);text-align:center}
  .sky-body .rule{left:8px;width:164px}
  .sky-body .headline{position:absolute;left:0;width:180px}
  .sky-cta{position:absolute;left:0;top:494px;width:180px;height:180px;background:radial-gradient(ellipse at 50% 50%, var(--red), var(--red-deep));color:var(--white);text-align:center;padding-top:22px}
  .sky-cta p{font-weight:800;line-height:1.12;text-transform:uppercase}

  /* 728 x 90 leaderboard */
  .leader{left:330px;top:55px;width:818px;height:101px;background:var(--ink-dark)}
  .leader-brand{position:absolute;left:0;top:0;width:293px;height:101px;background:linear-gradient(var(--panel-dark-top),var(--panel-dark) 70%,#161616)}
  .leader-brand .brand-mark{left:11px;top:11px;width:80px;height:80px}
  .leader-brand .brand-name{left:114px;top:4px;font-size:21px}
  .leader-brand .headline{position:absolute;left:114px;color:var(--white);width:170px;text-align:center}
  .leader-stripe{position:absolute;left:293px;top:0;width:12px;height:101px;background:linear-gradient(90deg,var(--red-deep),var(--red),#333)}
  .leader-features{position:absolute;left:305px;top:0;width:301px;height:101px;background:linear-gradient(90deg,var(--grey-feature),#a8a8a8 60%,var(--grey-feature-dark))}
  .leader-features .feature-list{left:14px;top:7px;font-size:17.5px;line-height:21.5px}
  .leader-cta{position:absolute;left:614px;top:0;width:204px;height:101px;background:radial-gradient(ellipse at 50% 40%, var(--red), var(--red-deep));color:var(--white);text-align:center;padding-top:6px}
  .leader-cta p{font-size:13px;font-weight:800;line-height:18px;text-transform:uppercase}

  /* 300 x 250 rectangle */
  .rect{left:571px;top:372px;width:337px;height:281px;background:var(--ink-dark)}
  .rect-top{position:absolute;left:0;top:0;width:337px;height:181px;background:linear-gradient(var(--panel-dark-top),var(--panel-dark) 70%,#161616)}
  .rect-top .brand-mark{left:9px;top:15px;width:148px;height:148px}
  .rect-top .brand-name{right:9px;top:7px;font-size:21.5px}
  .rect-top .headline{position:absolute;left:165px;width:160px;text-align:center;color:var(--white)}
  .rect-redline{position:absolute;left:0;top:181px;width:337px;height:6px;background:linear-gradient(var(--red),var(--red-deep))}
  .rect-features{position:absolute;left:0;top:187px;width:337px;height:94px;background:linear-gradient(90deg,var(--grey-feature-dark),#a0a0a0 50%,var(--grey-feature))}
  .rect-features .feature-list{left:17px;top:3px;font-size:17.5px;line-height:21.5px}
</style>
</head>
<body>

<svg width="0" height="0" style="position:absolute" aria-hidden="true">
  <symbol id="tick" viewBox="0 0 20 20">
    <path d="M2 11 L7 16 L18 3" fill="none" stroke="#fff" stroke-width="3.6" stroke-linecap="round" stroke-linejoin="round"/>
  </symbol>
</svg>

<!-- 160 x 600 -->
<section class="banner sky" aria-label="GuardNestly skyscraper banner">
  <div class="sky-top">
    <span class="brand-mark"></span>
    <span class="brand-name">GuardNestly</span>
  </div>
  <div class="sky-redline"></div>
  <div class="sky-body">
    <span class="rule" style="top:20px"></span>
    <span class="headline" style="top:26px;font-size:37px">Website</span>
    <span class="headline" style="top:62px;font-size:32px">Malware</span>
    <span class="headline" style="top:94px;font-size:23px">Monitoring</span>
    <span class="rule" style="top:122px"></span>
    <span class="headline" style="top:133px;font-size:26px">Automated</span>
    <span class="headline" style="top:158px;font-size:34px">Cleanup</span>
    <span class="rule" style="top:200px"></span>
    <a class="btn-learn" style="left:15px;top:203px;width:152px;height:47px;font-size:20px">LEARN MORE</a>
  </div>
  <div class="sky-cta">
    <p style="font-size:21px">Protect your</p>
    <p style="font-size:21px">website and</p>
    <p style="font-size:17.5px;line-height:1.35">Friendbook wall</p>
    <p style="font-size:20px">from hacker</p>
    <p style="font-size:32px;line-height:1.05">Attacks</p>
  </div>
</section>
<div class="size-label" style="left:54px;top:746px">160 x 600</div>

<!-- 728 x 90 -->
<section class="banner leader" aria-label="GuardNestly leaderboard banner">
  <div class="leader-brand">
    <span class="brand-mark"></span>
    <span class="brand-name">GuardNestly</span>
    <span class="rule" style="left:114px;top:31px;width:170px;background:var(--red)"></span>
    <span class="headline" style="top:35px;font-size:28px">Website</span>
    <span class="headline" style="top:60px;font-size:25px">Malware</span>
    <span class="headline" style="top:82px;font-size:18px">Monitoring</span>
  </div>
  <div class="leader-stripe"></div>
  <div class="leader-features">
    <ul class="feature-list">
      <li><svg><use href="#tick"/></svg>Automatic Cleanup</li>
      <li><svg><use href="#tick"/></svg>Friendbook Protection</li>
      <li><svg><use href="#tick"/></svg>Find Security Vulnerabilities</li>
      <li><svg><use href="#tick"/></svg>No Installation Needed</li>
    </ul>
  </div>
  <div class="leader-cta">
    <p>Protect your website</p>
    <p>and Friendbook wall</p>
    <p>from hacker attacks</p>
    <a class="btn-learn is-dark" style="left:26px;top:62px;width:153px;height:33px;font-size:20px">LEARN MORE</a>
  </div>
</section>
<div class="size-label" style="left:639px;top:170px">728 x 90</div>

<!-- 300 x 250 -->
<section class="banner rect" aria-label="GuardNestly medium rectangle banner">
  <div class="rect-top">
    <span class="brand-mark"></span>
    <span class="brand-name">GuardNestly</span>
    <span class="headline" style="top:41px;font-size:33px">Website</span>
    <span class="headline" style="top:73px;font-size:30px">Malware</span>
    <span class="headline" style="top:100px;font-size:21px">Monitoring</span>
    <span class="rule" style="left:165px;top:129px;width:160px;background:var(--red)"></span>
    <a class="btn-learn" style="left:167px;top:137px;width:153px;height:37px;font-size:20px">LEARN MORE</a>
  </div>
  <div class="rect-redline"></div>
  <div class="rect-features">
    <ul class="feature-list">
      <li><svg><use href="#tick"/></svg>Automatic Cleanup</li>
      <li><svg><use href="#tick"/></svg>Friendbook Protection</li>
      <li><svg><use href="#tick"/></svg>Find Security Vulnerabilities</li>
      <li><svg><use href="#tick"/></svg>No Installation Needed</li>
    </ul>
  </div>
</section>
<div class="size-label" style="left:639px;top:666px">300 x 250</div>

</body>
</html>
```